Korvexa - Adventurous, Fun, Exciting, Social Fitness Club needs a Webpage with attitude!

Korvexa... we're a fun, social, outdoor fitness club that needs not just a homepage designed for our website, but in the process a "personality" for our unique, innovative and cheeky brand.
We pride ourselves on getting our members outdoors trying new, exciting physical activities in an effort to find joy in an active lifestyle, and sharing that experience with other like minded people. We offer:
- Personal Training (1-on-1 Fitness Training)
- Group Fitness Classes (Boxing, Pilates, etc)
- Boot Camps (Military Style - Sandbags, Ropes, Tyres, etc)
- Events (Fun Runs, Triathlons, Ocean Swims, Treks, etc)
- Adventures(Machu Picchu Trek, Rock Climbing, Kayaking, etc)
Our tag line is 'No Judgements. No Limits!' The homepage should be exciting, adventurous and innovative, illustrating the values of our brand: possibility, thirst for life, personal accomplishment & freedom. It should be fun, friendly & inviting.
A few of our key benefits to members are:
- No Boring Workouts
- No Joining Fees or Long Term Contracts
- Results Guaranteed
The links below should give you a rough idea of the sort of "feel" we're after (vibrant, active, adventurous ).
http://www.pupiljourneys.com.au/
http://www.layoutgoblin.com/website-templates/31924.html
http://www.layoutgoblin.com/website-templates/32751.html
http://www.pivel.com/
Target Market(s)
Real, Everyday People - Men & Women (30:70) aged mainly between 21-40, who want a more exciting and enjoyable fitness experience than your typical gym offers.
Industry/Entity Type
Fitness
Requirements
Must have
- Strong, uplifting and motivating images of people enjoying fitness/physical activities outdoors

```html
<!DOCTYPE html>
<html lang="en">
<head>
<meta charset="utf-8">
<title>Korvexa – Outdoor Fitness Club</title>
<link href="https://fonts.googleapis.com/css2?family=PT+Sans:wght@400;700&family=Russo+One&display=swap" rel="stylesheet">
<style>
:root{
  --orange:#f7a000;
  --orange-light:#ffc21a;
  --orange-dark:#e07800;
  --ink:#111;
  --panel:#000;
  --paper:#fff;
  --bg-top:#ececec;
  --bg-bottom:#1b1b1b;
  --text:#2b2b2b;
}
*{box-sizing:border-box;margin:0;padding:0}
html,body{width:1037px;height:1200px;overflow:hidden}
body{
  position:relative;
  font-family:"PT Sans",sans-serif;
  color:var(--text);
  background:linear-gradient(var(--bg-top) 0 201px,var(--bg-bottom) 201px);
}
.abs{position:absolute}
a{color:inherit;text-decoration:none}

/* header */
.brand{left:128px;top:34px;font-family:"Russo One",sans-serif;font-size:46px;color:var(--orange);letter-spacing:1px;line-height:1}
.account{left:829px;top:9px;font-size:11px;font-weight:700;color:var(--ink)}
.account span{margin:0 8px}
.phone{left:722px;top:28px;width:201px;height:22px;background:var(--panel);border-radius:3px;color:var(--orange-light);font-weight:700;font-size:20px;line-height:22px;padding-left:48px}
.phone-icon{position:absolute;left:11px;top:-3px;width:26px;height:28px;background:var(--orange);border-radius:4px;border:2px solid var(--panel)}
.page{left:113px;top:62px;width:810px;height:1111px;background:var(--paper);border:1px solid #444;border-radius:8px}
.utility{left:617px;top:83px;font-size:11px;font-weight:700;color:var(--ink);display:flex;align-items:center;gap:6px}
.utility .sep{margin:0 10px}
.select{width:106px;height:18px;background:var(--panel);border-radius:3px;color:#fff;font-weight:400;font-size:10px;line-height:18px;padding-left:8px;position:relative}
.select::after{content:"";position:absolute;right:7px;top:6px;border:5px solid transparent;border-top:7px solid #fff}

/* nav */
.nav{left:113px;top:124px;width:810px;height:34px;background:linear-gradient(#2a2a2a,#0b0b0b)}
.nav a{position:absolute;top:0;height:34px;line-height:34px;font-size:11px;font-weight:700;color:var(--orange);text-transform:uppercase}
.nav .current{left:9px;top:6px;height:22px;line-height:22px;width:68px;background:var(--orange);color:var(--ink);text-align:center}
.nav i{position:absolute;top:0;width:1px;height:34px;background:#444}
.social{position:absolute;top:8px;width:18px;height:18px;border-radius:3px;background:var(--orange)}

/* hero */
.hero{left:121px;top:164px;width:798px;height:280px;background:var(--panel)}
.hero-photo{position:absolute;left:6px;top:8px;width:537px;height:265px;background:linear-gradient(120deg,#f6f0d8,#f2d45a 55%,#c79a3a)}
.offer{position:absolute;left:565px;top:20px;color:var(--orange);font-weight:700;line-height:1}
.offer .t1{font-size:16px}
.offer .t2{font-size:22px;margin-top:1px}
.perks{position:absolute;left:568px;top:65px;list-style:none;color:#fff;font-size:11px;font-weight:700}
.perks li{height:24px;padding-left:16px;position:relative}
.perks li::before{content:"»";position:absolute;left:0;top:-3px;color:var(--orange);font-size:14px}
.field{position:absolute;background:#fff;border-radius:3px;font-size:10px;color:#444;padding-left:13px;line-height:21px;height:21px}
.btn{position:absolute;background:linear-gradient(var(--orange-light),var(--orange-dark));border-radius:6px;color:var(--ink);font-weight:700}

/* features */
.feature-tab{left:130px;top:471px;width:30px;height:192px;background:var(--orange)}
.feature-tab span{position:absolute;left:-38px;top:84px;transform:rotate(-90deg);font-weight:700;font-size:20px;color:var(--ink);letter-spacing:1px;width:110px;text-align:center}
.card{top:471px;width:239px;height:189px;background:var(--panel);color:#fff}
.card .shot{position:absolute;left:9px;top:9px;width:221px;height:92px}
.card h3{position:absolute;left:9px;top:110px;font-size:17px;color:var(--orange);font-weight:700}
.card p{position:absolute;left:9px;top:134px;font-size:10.5px;line-height:14px;width:200px}
.card .more{position:absolute;right:15px;top:167px;font-size:10.5px;color:var(--orange)}
.rule{left:130px;top:688px;width:777px;height:1px;background:#222}

/* content */
.heading{height:24px;background:var(--panel);color:#fff;font-weight:700;font-size:17px;line-height:24px;padding-left:10px}
.copy{font-size:11.6px;line-height:13.7px;color:var(--text)}
.copy p+p{margin-top:13px}
.copy em{font-style:normal;font-weight:700;color:var(--orange-dark)}
.side-title{font-size:17px;font-weight:700;color:var(--ink);display:flex;align-items:center;gap:8px}
.video{left:688px;top:747px;width:219px;height:147px;background:var(--panel)}
.video-still{position:absolute;left:7px;top:7px;width:206px;height:135px;background:linear-gradient(110deg,#9ea4a0,#6c716c 55%,#8b6b4e)}
.play{position:absolute;left:93px;top:56px;width:26px;height:26px;border-radius:50%;background:rgba(255,255,255,.8)}
.play::after{content:"";position:absolute;left:10px;top:7px;border:6px solid transparent;border-left:8px solid #555}
.newsletter{left:688px;top:950px;width:219px;height:88px;background:var(--panel)}

/* footer */
.footer{left:117px;top:1081px;width:804px;height:47px;background:linear-gradient(#333,#1e1e1e)}
.footer ul{list-style:none;display:flex;justify-content:center;gap:19px;padding-top:17px;font-size:10px;color:#ddd}
.footer li::before{content:"• "}
.legal{left:113px;top:1145px;width:810px;text-align:center;font-size:9px;color:#222}
</style>
</head>
<body>

<div class="abs page"></div>

<a class="abs brand" href="#">KORVEXA</a>
<div class="abs account"><a href="#">Login</a><span>|</span><a href="#">Register</a></div>
<div class="abs phone"><span class="phone-icon"></span>1300 555 019</div>

<div class="abs utility">
  <svg width="20" height="20" viewBox="0 0 20 20" aria-hidden="true"><circle cx="10" cy="10" r="8.5" fill="none" stroke="#111" stroke-width="2.5"/><path d="M10 5v5l3 2" stroke="#111" stroke-width="2" fill="none"/></svg>
  <span>Timetable</span><span class="sep">|</span><span>Club Locations:</span>
  <div class="select">Melbourne</div>
</div>

<nav class="abs nav">
  <a class="current" href="#">Home</a>
  <i style="left:85px"></i>
  <a style="left:110px" href="#">About Us</a>
  <i style="left:185px"></i>
  <a style="left:211px" href="#">Fitness</a>
  <i style="left:277px"></i>
  <a style="left:303px" href="#">Events &amp; Adventures</a>
  <i style="left:446px"></i>
  <a style="left:469px" href="#">Contact Us</a>
  <span class="social" style="left:716px"></span>
  <span class="social" style="left:739px"></span>
  <span class="social" style="left:761px"></span>
  <span class="social" style="left:784px"></span>
</nav>

<section class="abs hero">
  <div class="hero-photo" role="img" aria-label="Two smiling children in yellow sports shirts lying on the grass with a soccer ball"></div>
  <div class="offer"><div class="t1">FREE Membership:</div><div class="t2">(Valued $65)</div></div>
  <ul class="perks">
    <li>Monthly E-News Hints, Tips &amp; Advice</li>
    <li>VIP Invites Events &amp; Adventures</li>
    <li>Special Member Only Offers</li>
    <li>Discounts Card to 20+ Providers</li>
  </ul>
  <div class="field" style="left:568px;top:168px;width:201px">Your Name</div>
  <div class="field" style="left:568px;top:196px;width:201px">Your Email Address</div>
  <div class="btn" style="left:568px;top:230px;width:130px;height:28px;font-size:15px;line-height:28px;padding-left:18px">» JOIN US</div>
</section>

<div class="abs feature-tab"><span>FEATURES</span></div>

<article class="abs card" style="left:163px">
  <div class="shot" role="img" aria-label="Smiling man exercising outdoors in a park with a group behind him" style="background:linear-gradient(100deg,#7fae4a,#b9c9a0 45%,#6a5a4a)"></div>
  <h3>Personal Training</h3>
  <p>FREE Initial Consult &amp; 1-on-1 Session (Valued &amp;80.00)</p>
  <a class="more" href="#">+ MORE</a>
</article>
<article class="abs card" style="left:416px">
  <div class="shot" role="img" aria-label="Group of smiling women at an outdoor fitness class" style="background:linear-gradient(100deg,#e9d9b0,#c7d8a0 50%,#e8b8c8)"></div>
  <h3>Group Fitness</h3>
  <p>Intro Pass &amp; 255 7 Days Unlimited Classes</p>
  <a class="more" href="#">+ MORE</a>
</article>
<article class="abs card" style="left:668px">
  <div class="shot" role="img" aria-label="Determined man in a black training shirt mid workout" style="background:linear-gradient(100deg,#2a2a2a,#8a6a58 55%,#3a3a3a)"></div>
  <h3>Boot Camp</h3>
  <p>Starts Soon Bookings are Limited</p>
  <a class="more" href="#">+ MORE</a>
</article>

<div class="abs rule"></div>

<h2 class="abs heading" style="left:132px;top:711px;width:258px">Personal Trainers in Brisbane</h2>
<div class="abs copy" style="left:141px;top:743px;width:526px">
  <p>If you are exercising and have committed a good chunk of time into your fitness, you want to make sure you get the best returns possible. This is where a personal trainer can help. In personal training sessions you will be pushed to achieve your personal best, meaning that you get the best results, both physically and mentally, from your fitness training.</p>
  <p>For those that are new to exercising, it can be difficult to know where to begin. Having a <em>personal trainer</em> on board will give you the guidance and support that you need. Those that enlist the help of a personal trainer often find that they achieve much better results than those that go it alone, and often in a much shorter space of time.</p>
</div>

<h2 class="abs heading" style="left:132px;top:884px;width:388px">Personal Training Locations Around Brisbane</h2>
<div class="abs copy" style="left:144px;top:915px;width:523px">
  <p>If you are lucky enough to enjoy Brisbane’s perfect climate then you shouldn’t miss the chance to do some outdoor exercise. In the CBD you can enjoy a before work session at the Roma Street Parkland or the Brisbane City Botanic Gardens. About fifteen minutes out of town is the Mt Coot-tha Botanic Gardens which boast themed gardens and excellent tracks for walking and running. With plenty of beautiful parks around Brisbane’s CBD, you don’t need to worry about missing out on training just because of your long work hours.</p>
  <p>Just because you live in the suburbs, doesn’t mean that you need to miss out on personal training either. Right around Brisbane and surrounds there are hundreds of personal trainers organizing classes in parks and in gyms and fitness studios.</p>
</div>

<h2 class="abs side-title" style="left:687px;top:711px">
  <svg width="26" height="24" viewBox="0 0 26 24" aria-hidden="true"><rect x="1" y="8" width="24" height="15" fill="#111"/><path d="M1 3l23-3 1 6-23 3z" fill="#111"/><path d="M7 2l3 5M13 1l3 5M19 0l3 5" stroke="#fff" stroke-width="1.5"/><path d="M10 12v8l7-4z" fill="#4a9ad8"/></svg>
  Watch Video
</h2>
<div class="abs video">
  <div class="video-still" role="img" aria-label="Woman stretching on a road before an outdoor run"><span class="play"></span></div>
</div>

<h2 class="abs side-title" style="left:687px;top:913px">
  <svg width="32" height="28" viewBox="0 0 32 28" aria-hidden="true"><path d="M2 8l26-6 3 18-26 6z" fill="#dfeef8" stroke="#2a6aa0" stroke-width="1.5"/><path d="M2 8l15 9 11-15" fill="none" stroke="#2a6aa0" stroke-width="1.5"/></svg>
  Newsletter
</h2>
<div class="abs newsletter">
  <div class="field" style="left:14px;top:23px;width:191px">Your Email Address</div>
  <div class="btn" style="left:15px;top:53px;width:105px;height:22px;font-size:14px;line-height:22px;padding-left:13px;font-weight:400">Subscribe</div>
</div>

<footer class="abs footer">
  <ul><li>Home</li><li>About Us</li><li>Fitness</li><li>Events &amp; Adventures</li><li>Contact Us</li></ul>
</footer>
<p class="abs legal">Copyrights ©2011. Korvexa. All Rights Reserved.</p>

</body>
</html>
```